Help me create an amazing cover for my first ebook!!

I am looking to have a modern and professional looking cover for my first ebook. It will be published through Borvex Quill Self Press and will need to follow their formatting and guidelines. I want the cover to have a modern and vibrant feel, that appeals to a millennial audience. This is a real estate book that is focused on a niche category catered to young professionals, so the idea would be to appeal to them.

Title:
The Twentysomething Playbook for Duplex Living

A Smart Property Buying Plan to Start Early, Cut Your Housing Costs (Sometimes to Zero), and Speed Up Your Path to Lasting Wealth.

Davin Osterlund

Target Market(s)

Real Estate investors, investors, millennials, young professionals, college educated, 20-40 years old.Financial freedom, finance.

Industry/Entity Type

Real Estate

Font styles to use
Sans Serif

Colors

Designer to choose colors to be used in the design.

Requirements
Must have
• Must follow the borvex quill self press format. I attached a screenshot of the details, it can also be found here: https://qsp.borvexbooks.example/en_US/help/topic/R481736025
• Must include this title:
• The Twentysomething Playbook for Duplex Living
• A Smart Property Buying Plan to Start Early, Cut Your Housing Costs (Sometimes to Zero), and Speed Up Your Path to Lasting Wealth.
• Davin Osterlund.
• I added examples of book covers I like to use as a guide, I also added some color pallette examples.
Nice to have
• Modern, clean design that's not too busy. Some sort of simple photo or illustration to incorporate in the cover along with the text would be nice.

```html
<!DOCTYPE html>
<html lang="en">
<head>
<meta charset="utf-8">
<title>The Twentysomething Playbook for Duplex Living — Cover</title>
<link rel="stylesheet" href="https://fonts.googleapis.com/css2?family=Oswald:wght@600&family=Open+Sans:wght@800&family=Montserrat:wght@500&display=swap">
<style>
  :root {
    --blue-deep: #0a4f82;
    --blue-mid: #1678b3;
    --blue-light: #2f9ad2;
    --ink-white: #ffffff;
    --subtitle-blue: #c4e6f6;
    --art-light: #e9eef2;
    --art-mid: #9fb3c2;
    --art-dark: #3c4c5a;
  }
  * { margin: 0; padding: 0; box-sizing: border-box; }
  html, body {
    width: 800px;
    height: 1200px;
    overflow: hidden;
    background: var(--blue-mid);
  }
  .book-cover {
    position: relative;
    width: 800px;
    height: 1200px;
    overflow: hidden;
    background: radial-gradient(ellipse at 50% 45%, var(--blue-light) 0%, var(--blue-mid) 50%, var(--blue-deep) 100%);
  }
  .title-block {
    position: absolute;
    left: 0;
    top: 0;
    width: 800px;
    height: 490px;
    z-index: 2;
  }
  .title-kicker, .title-main {
    font-family: "Oswald", "Arial Narrow", sans-serif;
    font-weight: 600;
    fill: var(--ink-white);
    text-transform: uppercase;
  }
  .subtitle {
    font-family: "Open Sans", Arial, sans-serif;
    font-weight: 800;
    fill: var(--subtitle-blue);
    letter-spacing: 0.5px;
  }
  .cover-art {
    position: absolute;
    left: 130px;
    top: 495px;
    width: 580px;
    height: 505px;
    z-index: 1;
    border-radius: 40% 40% 45% 35%;
    background: radial-gradient(ellipse at 35% 40%, var(--art-light) 0%, var(--art-mid) 45%, rgba(60, 76, 90, 0.35) 75%, rgba(60, 76, 90, 0) 100%);
  }
  .author-name {
    position: absolute;
    left: 0;
    top: 1110px;
    width: 800px;
    text-align: center;
    font-family: "Montserrat", Arial, sans-serif;
    font-weight: 500;
    font-size: 40px;
    letter-spacing: 6px;
    color: var(--ink-white);
    text-transform: uppercase;
  }
</style>
</head>
<body>
  <main class="book-cover">
    <div class="cover-art" role="img" aria-label="Illustration of a tall ceramic canal house tilted over, being pulled by a rope held by a small man in a shirt and tie"></div>

    <svg class="title-block" width="800" height="490" viewBox="0 0 800 490" aria-label="The Twentysomething Playbook for Duplex Living">
      <g transform="rotate(-4 400 250)">
        <text class="title-kicker" x="400" y="135" font-size="64" text-anchor="middle" textLength="680" lengthAdjust="spacingAndGlyphs">THE TWENTYSOMETHING PLAYBOOK FOR</text>
        <text class="title-main" x="400" y="318" font-size="184" text-anchor="middle" textLength="720" lengthAdjust="spacingAndGlyphs">DUPLEX LIVING</text>
        <g class="subtitle" font-size="25" text-anchor="middle">
          <text x="405" y="370" textLength="620" lengthAdjust="spacingAndGlyphs">A SMART PROPERTY BUYING PLAN TO START</text>
          <text x="405" y="399" textLength="650" lengthAdjust="spacingAndGlyphs">EARLY, CUT YOUR HOUSING COSTS (SOMETIMES</text>
          <text x="405" y="428" textLength="670" lengthAdjust="spacingAndGlyphs">TO ZERO), AND SPEED UP YOUR PATH TO LASTING</text>
          <text x="405" y="457">WEALTH.</text>
        </g>
      </g>
    </svg>

    <p class="author-name">Davin Osterlund</p>
  </main>
</body>
</html>
```